UPDATE: I have uploaded the selected logo from the other contest, please use it in your designs.

I have a logo design contest as well so not sure how ArtHive handles that. They should integrate at some point. I will describe the overall theme with the logo description. See it for details.

The business card side of it would just build on that same theme.

Target Market(s)

8-40

Industry/Entity Type

Business

Contact Information for Business Card

FirstName LastName
Email

Logo Text

VelMarin

Font styles to use
Sans Serif

Requirements
Must have
• the url VelMarin.com somewhere in it.

```html
<!DOCTYPE html>
<html lang="en">
<head>
<meta charset="utf-8">
<title>VelMarin Business Card</title>
<link rel="stylesheet" href="https://fonts.googleapis.com/css2?family=Open+Sans:wght@400;600;700&display=swap">
<style>
  :root {
    --backdrop: #1e1e20;
    --card-front: #ffffff;
    --card-back: #f3f3f3;
    --orange: #f39a1e;
    --blue: #1d74c2;
    --white: #ffffff;
  }
  * { margin: 0; padding: 0; box-sizing: border-box; }
  html, body {
    width: 1200px;
    height: 800px;
    overflow: hidden;
    background: var(--backdrop);
    font-family: "Open Sans", sans-serif;
  }
  .stage {
    width: 1200px;
    height: 800px;
    display: flex;
    align-items: center;
    justify-content: center;
    gap: 60px;
  }
  .card {
    position: relative;
    width: 520px;
    height: 297px;
    overflow: hidden;
  }
  .card--front { background: var(--card-front); }
  .card--back { background: var(--card-back); }

  .wordmark {
    font-weight: 700;
    color: var(--orange);
    letter-spacing: 0.5px;
    line-height: 1;
  }
  .card--front .wordmark {
    position: absolute;
    inset: 0;
    display: flex;
    align-items: center;
    justify-content: center;
    font-size: 64px;
  }

  .band {
    position: absolute;
    height: 14px;
    background: var(--orange);
  }
  .band--top { left: 150px; right: 0; top: 30px; }
  .band--left { left: 0; width: 92px; top: 70px; }
  .band--middle { left: 260px; right: 22px; top: 172px; }
  .band--bottom { left: 0; right: 0; top: 256px; }

  .name-plate {
    position: absolute;
    left: 92px;
    top: 44px;
    width: 150px;
    height: 40px;
    background: var(--blue);
    padding: 4px 0 0 32px;
  }
  .name-plate__name {
    display: block;
    color: var(--orange);
    font-weight: 700;
    font-size: 15px;
    line-height: 1.1;
  }
  .name-plate__title {
    display: block;
    color: var(--white);
    font-size: 10px;
    line-height: 1.3;
  }

  .card--back .wordmark {
    position: absolute;
    left: 120px;
    top: 135px;
    font-size: 26px;
  }

  .contact {
    position: absolute;
    left: 300px;
    top: 86px;
    list-style: none;
    color: var(--orange);
    font-size: 11.5px;
    line-height: 1;
  }
  .contact li + li { margin-top: 18px; }
</style>
</head>
<body>
  <main class="stage">
    <section class="card card--front" aria-label="Business card front">
      <div class="wordmark">VelMarin</div>
    </section>

    <section class="card card--back" aria-label="Business card back">
      <div class="band band--top"></div>
      <div class="band band--left"></div>
      <div class="name-plate">
        <span class="name-plate__name">Lena Morrow</span>
        <span class="name-plate__title">Manager</span>
      </div>
      <div class="wordmark">VelMarin</div>
      <ul class="contact">
        <li>Url:VelMarin.com</li>
        <li>Phoon:00 987 654 321</li>
        <li>Email:lena@velmarin.com</li>
      </ul>
      <div class="band band--middle"></div>
      <div class="band band--bottom"></div>
    </section>
  </main>
</body>
</html>
```